Full color cover for Chamber's Membership Menu

I need a cover, 8 1/2" x 11" for our Chamber of Commerce Membership Menu. Is should have our logo and the words, Membership Menu on it. That's all that is necessary but it can include one or more of the other photos (maybe a college?) that I added, though they are not required. Our logo colors should be used: 37-170-226, 58-181-74, 40-56-144, 247-148-29, 189-190-192.

Target Market(s)

Business owners and managers

Industry/Entity Type

Business Development

Font styles to use
Serif

Colors
0054AA
0677BA
7BADD7
CADEEF
E8F1F8
00AB8E
00BBA5
67D7C9
C6EFE9
E9F9F6
F0912C
F2A743
F7CA91
FBE8D2
FDF5EE

Requirements
Must have
• Our logo and the words Membership Menu
Nice to have
• An attractive business-like feel. It can be very simple.

```html
<!DOCTYPE html>
<html lang="en">
<head>
<meta charset="utf-8">
<title>Membership Menu Cover</title>
<link rel="stylesheet" href="https://fonts.googleapis.com/css2?family=Roboto:wght@500&family=Montserrat:wght@300&display=swap">
<style>
  :root {
    --chamber-blue: #25aae2;
    --chamber-navy: #28388f;
    --chamber-grey: #bdbec0;
    --paper-light: #fbfbfb;
    --paper-mid: #ececec;
    --title-grey: #4a4a4a;
  }
  html, body {
    margin: 0;
    padding: 0;
    width: 847px;
    height: 1200px;
    overflow: hidden;
  }
  .cover {
    position: relative;
    width: 847px;
    height: 1200px;
    background: radial-gradient(ellipse at 50% 40%, var(--paper-light) 0%, var(--paper-mid) 100%);
    overflow: hidden;
  }
  .cover-art {
    position: absolute;
    inset: 0;
    width: 847px;
    height: 1200px;
  }
  .brand {
    position: absolute;
    top: 78px;
    left: 0;
    width: 847px;
    text-align: center;
    color: var(--chamber-navy);
    font-family: "Roboto", Arial, sans-serif;
    font-weight: 500;
  }
  .brand-dot {
    width: 96px;
    height: 96px;
    margin: 0 auto 34px;
    border-radius: 50%;
    background: var(--chamber-blue);
  }
  .brand-name {
    margin: 0;
    font-size: 34px;
    line-height: 1;
    letter-spacing: 0.01em;
  }
  .brand-tagline {
    margin: 6px 0 0;
    font-size: 16px;
    line-height: 1;
    letter-spacing: 0.4em;
    text-indent: 0.4em;
  }
  .cover-title {
    position: absolute;
    top: 1050px;
    left: 0;
    width: 847px;
    margin: 0;
    text-align: center;
    font-family: "Montserrat", Arial, sans-serif;
    font-weight: 300;
    font-size: 26px;
    letter-spacing: 0.78em;
    text-indent: 0.78em;
    color: var(--title-grey);
  }
</style>
</head>
<body>
<main class="cover">
  <svg class="cover-art" viewBox="0 0 680 880" preserveAspectRatio="none">
    <defs>
      <linearGradient id="photo-main" x1="0" y1="0" x2="0" y2="1">
        <stop offset="0" stop-color="#7fb79a"/>
        <stop offset="0.55" stop-color="#6a5a5a"/>
        <stop offset="1" stop-color="#8a6a4c"/>
      </linearGradient>
      <linearGradient id="photo-event" x1="0" y1="0" x2="0" y2="1">
        <stop offset="0" stop-color="#7a5638"/>
        <stop offset="1" stop-color="#2a2426"/>
      </linearGradient>
    </defs>

    <polygon class="band" points="0,322 680,322 680,560 340,640 0,565" fill="var(--chamber-blue)"/>
    <polygon class="band-shadow" points="70,655 340,720 610,655 610,648 340,708 70,648" fill="var(--chamber-grey)"/>

    <g role="img" aria-label="Group photo of a ribbon cutting at a member business">
      <polygon points="48,226 631,226 631,468 340,530 48,468" fill="url(#photo-main)"/>
    </g>
    <g role="img" aria-label="Photo of members at a networking event">
      <polygon points="70,528 235,528 235,680 70,645" fill="url(#photo-event)"/>
    </g>
    <g role="img" aria-label="Photo of members at an evening reception">
      <polygon points="257,565 422,565 422,695 340,705 257,695" fill="url(#photo-event)"/>
    </g>
    <g role="img" aria-label="Photo of restaurant staff in aprons">
      <polygon points="444,528 610,528 610,645 444,680" fill="url(#photo-event)"/>
    </g>
  </svg>

  <header class="brand">
    <div class="brand-dot"></div>
    <p class="brand-name">RIVERTON CHAMBER</p>
    <p class="brand-tagline">OF COMMERCE &amp; TOURISM</p>
  </header>

  <h1 class="cover-title">MEMBERSHIP MENU</h1>
</main>
</body>
</html>
```